Real estate business needing a creative mind!

Have a real estate business called Brightwell Estates LLC. I need some business card with custom logo. That logo can be an intricate design of a house or houses. Maybe some blue and orange colors, maybe the business name in orange. Some thing that leaves a wow impression to the holder. Or just surprise me! Must have business name, name, email and phone number.

Target Market(s)

Property sellers and real estate professionals

Industry/Entity Type

Real estate

Contact Information for Business Card

Want it to stand out but also be professional.

Colors

Designer to choose colors to be used in the design.

Requirements
Must have
• Business name Brightwell Estates. My name which is Dalton Meese. The business email which is Brightwellestates1@novamail.example. The phone number which is 555-014-2297
Nice to have
• Could be a logo of the name over some mountain houses being that we live by the Smokey mountains. Could have a sun if it looks ok?

```html
<!DOCTYPE html>
<html lang="en">
<head>
<meta charset="utf-8">
<title>Brightwell Estates LLC – Business Cards</title>
<link rel="stylesheet" href="https://fonts.googleapis.com/css2?family=Audiowide&family=Poppins:wght@400;500&display=swap">
<style>
  :root {
    --bg: #e9e9ee;
    --royal: #2f2f9a;
    --royal-light: #4545b4;
    --orange: #f07d1a;
    --white: #ffffff;
    --ink: #2f2f9a;
  }
  * { margin: 0; padding: 0; box-sizing: border-box; }
  html, body { width: 1200px; height: 880px; overflow: hidden; background: var(--bg); }
  .canvas { position: relative; width: 1200px; height: 880px; }

  .card {
    position: absolute;
    width: 640px;
    height: 366px;
    border-radius: 22px;
    overflow: hidden;
    box-shadow: 0 10px 28px rgba(0,0,0,0.18);
  }
  .card-front {
    left: 60px; top: 60px;
    background: linear-gradient(135deg, var(--royal-light) 0%, var(--royal) 45%, var(--royal) 100%);
  }
  .card-back { left: 500px; top: 454px; background: var(--white); }
  .card-shapes { position: absolute; inset: 0; width: 100%; height: 100%; }

  .brand {
    position: absolute;
    font-family: "Audiowide", sans-serif;
    color: var(--orange);
    text-align: center;
    line-height: 1;
    letter-spacing: 1px;
  }
  .brand-name { display: block; }
  .brand-suffix { display: block; margin-top: 10px; letter-spacing: 3px; }

  .card-front .brand { left: 0; right: 0; top: 128px; }
  .card-front .brand-name { font-size: 54px; }
  .card-front .brand-suffix { font-size: 24px; }

  .card-back .brand { left: 110px; width: 400px; top: 80px; }
  .card-back .brand-name { font-size: 44px; }
  .card-back .brand-suffix { font-size: 20px; }

  .divider {
    position: absolute;
    left: 40px; top: 222px;
    width: 540px; height: 1.5px;
    background: var(--ink);
  }
  .email {
    position: absolute;
    right: 70px; top: 196px;
    display: flex; align-items: center; gap: 8px;
    font-family: "Poppins", sans-serif;
    font-size: 13px;
    color: var(--ink);
  }
  .person { position: absolute; left: 44px; top: 250px; }
  .person-name {
    font-family: "Audiowide", sans-serif;
    font-size: 24px;
    color: var(--ink);
    letter-spacing: 1px;
  }
  .person-title {
    font-family: "Audiowide", sans-serif;
    font-size: 15px;
    color: var(--orange);
    letter-spacing: 1px;
    margin-top: 2px;
  }
  .phone {
    display: flex; align-items: center; gap: 8px;
    margin-top: 8px;
    font-family: "Poppins", sans-serif;
    font-weight: 500;
    font-size: 19px;
    color: var(--ink);
  }
  .icon { width: 18px; height: 18px; flex: none; }
</style>
</head>
<body>
<main class="canvas">

  <section class="card card-front" aria-label="Card front">
    <div class="brand">
      <span class="brand-name">BRIGHTWELL</span>
      <span class="brand-suffix">ESTATES LLC</span>
    </div>
  </section>

  <section class="card card-back" aria-label="Card back">
    <svg class="card-shapes" viewBox="0 0 640 366" preserveAspectRatio="none" aria-hidden="true">
      <path fill="#2f2f9a" d="M420,0 H640 V366 H330 C360,342 390,332 430,332 H560 C596,332 612,306 612,268 V84 C612,54 594,30 560,30 H478 C446,30 446,0 420,0 Z"/>
      <path fill="#f07d1a" d="M0,344 H400 C430,344 440,352 452,366 H0 Z"/>
    </svg>

    <div class="brand">
      <span class="brand-name">BRIGHTWELL</span>
      <span class="brand-suffix">ESTATES LLC</span>
    </div>

    <div class="email">
      <svg class="icon" viewBox="0 0 20 20" aria-hidden="true">
        <circle cx="10" cy="10" r="10" fill="#f07d1a"/>
        <rect x="5" y="6.5" width="10" height="7" rx="1" fill="#fff"/>
        <path d="M5.5,7 L10,10.5 L14.5,7" fill="none" stroke="#f07d1a" stroke-width="1.2"/>
      </svg>
      <span>Brightwellestates1@novamail.example</span>
    </div>

    <div class="divider"></div>

    <div class="person">
      <div class="person-name">DALTON MEESE</div>
      <div class="person-title">REALTOR</div>
      <div class="phone">
        <svg class="icon" viewBox="0 0 20 20" aria-hidden="true">
          <circle cx="10" cy="10" r="10" fill="#f07d1a"/>
          <path fill="#fff" d="M7,5 L8.6,5 L9.4,7.6 L8.3,8.6 C8.9,10 10,11.1 11.4,11.7 L12.4,10.6 L15,11.4 L15,13 C15,14 14,14.8 13,14.6 C9,14 6,11 5.4,7 C5.2,6 6,5 7,5 Z"/>
        </svg>
        <span>555-014-2297</span>
      </div>
    </div>
  </section>

</main>
</body>
</html>
```